Design Challege - Simplify a Complex Message

We have a new website design, but one of the pages presents a particular problem.

Our company does ERP implementations. We have developed a proprietary approach to these implementations based on the idea that you must get eight (and only eight) things right. These eight things are listed below, summarized in one or two words each:

1. Value
2. Capability
3. Functionality
4. Data
5. Technology
6. Change Leadership
7. Quality
8. Governance

Each of these eight things can be summarized in a short paragraph, but when you combine all eight summaries with a brief introductory text, the result is a lot of text - so much text that the casual surfer may be overwhelmed by it.

The winning design will find an engaging way to present the information in a way that presents a high-level summary, using icons and one- or two-word descriptions above but revealing more information when clicked.

Our current design for this information, with a paragraph describing the eight elements in a table, is included as an upload in PDF and Microsoft Word formats. We are looking for a creative way to display these eight things, showing the detail only when the user wants to see it.

The website is being built in WordPress, using Elementor as a page builder.

We will implement (code) the page, but the winner will be asked to specify the widget or other add-in if one is required.

The design does not need to include a header or footer, we have those.

Target Market(s)

Business executives working in technology

Industry/Entity Type

Any

Number of Pages Required

1 page

Font styles to use
Sans Serif

Requirements
Must have
• A design for the body of the page, but not the header or footer.
Nice to have
• Unique icons or images appropriate for each of the eight things.
Should not have
• A lot of text on one page

```html
<!DOCTYPE html>
<html lang="en">
<head>
<meta charset="utf-8">
<title>ERP Implementations – Eight Things to Get Right</title>
<link href="https://fonts.googleapis.com/css2?family=Poppins:wght@400;600;700&display=swap" rel="stylesheet">
<style>
  :root{
    --bg:#f6f6f6;
    --green:#55a300;
    --green-dark:#3e7800;
    --ink:#111111;
    --text:#222222;
    --panel:#ffffff;
    --band:#efefef;
  }
  *{box-sizing:border-box;margin:0;padding:0}
  html,body{width:716px;height:1200px;overflow:hidden;background:var(--bg)}
  body{font-family:'Poppins',sans-serif;color:var(--text);position:relative}
  .intro-eyebrow{position:absolute;top:36px;left:0;width:716px;text-align:center;font-weight:700;font-size:25px;letter-spacing:.2px;color:var(--ink)}
  .intro-title{position:absolute;top:74px;left:0;width:716px;text-align:center;font-weight:400;font-size:27px;color:var(--ink)}
  .intro-sub{position:absolute;top:121px;left:0;width:716px;text-align:center;font-size:16px;color:var(--ink)}
  .intro-copy{position:absolute;top:159px;left:144px;width:480px;font-size:9.2px;line-height:14.3px;color:var(--ink);white-space:nowrap}
  .intro-copy p+p{margin-top:12px}
  .step{position:absolute;width:162px;height:420px}
  .step svg.tile{position:absolute;left:0;top:0;width:162px;height:420px;overflow:visible}
  .step-title{position:absolute;top:166px;left:0;width:162px;text-align:center;font-weight:600;font-size:12.3px;color:var(--ink);white-space:nowrap}
  .step-copy{position:absolute;top:196px;left:4px;width:154px;text-align:center;font-size:9.2px;line-height:14.3px;white-space:nowrap}
  .step-btn{position:absolute;top:271px;left:39px;width:81px;height:27px;border:1px solid #333;background:#fff;font-size:10.2px;line-height:25px;text-align:center;color:var(--ink)}
  .step-num{position:absolute;top:327px;left:56px;width:50px;text-align:center;font-weight:700;font-size:17px;color:var(--ink)}
</style>
</head>
<body>

<svg width="0" height="0" style="position:absolute" aria-hidden="true">
  <defs>
    <filter id="lift" x="-30%" y="-30%" width="160%" height="160%">
      <feDropShadow dx="0" dy="4" stdDeviation="4" flood-color="#000" flood-opacity=".25"/>
    </filter>
    <g id="tile">
      <rect x="16" y="74" width="130" height="90" fill="#fbfbfb"/>
      <rect x="0" y="154" width="162" height="156" fill="var(--panel)"/>
      <rect x="0" y="310" width="162" height="30" fill="var(--band)"/>
      <g filter="url(#lift)">
        <rect x="28.5" y="25.5" width="105" height="105" rx="12" transform="rotate(45 81 78)" fill="var(--green-dark)"/>
        <rect x="28.5" y="21.5" width="105" height="105" rx="12" transform="rotate(45 81 74)" fill="var(--green)"/>
      </g>
      <rect x="40" y="33" width="82" height="82" rx="8" transform="rotate(45 81 74)" fill="none" stroke="#fff" stroke-width="1.6"/>
      <g filter="url(#lift)">
        <path d="M3 344 H159 L86 410 Q81 414 76 410 Z" fill="var(--green-dark)"/>
        <path d="M3 340 H159 L86 405 Q81 409 76 405 Z" fill="var(--green)"/>
      </g>
      <path d="M20 350 L81 398 L142 350" fill="none" stroke="#fff" stroke-width="1.6"/>
      <circle cx="81" cy="340" r="25" fill="#fff"/>
      <circle cx="81" cy="340" r="20" fill="none" stroke="var(--green)" stroke-width="2"/>
    </g>
  </defs>
</svg>

<div class="intro-eyebrow">OUR SERVICES</div>
<div class="intro-title">ERP Implementations</div>
<div class="intro-sub">Eight Things to Get Right</div>
<div class="intro-copy">
  <p>Like the roots and branches of a tree, there are many considerations in an ERP implementation.<br>Focus too much on the minor details, and you can lose sight of the tree.</p>
  <p>In an ERP implementation, you must get eight major things right to be successful. Ignore any of them,<br>and your implementation will fail. Get them right, and you will likely succeed. .</p>
</div>

<!-- Row one -->
<div class="step" style="left:15px;top:270px">
  <svg class="tile" viewBox="0 0 162 420"><use href="#tile"/>
    <g fill="#fff"><circle cx="72" cy="67" r="13"/><circle cx="72" cy="67" r="10" fill="var(--green)"/>
    <text x="72" y="72" text-anchor="middle" font-size="14" font-family="Poppins,sans-serif" font-weight="600" fill="#fff">$</text>
    <rect x="82" y="57" width="16" height="3.5" rx="1.7"/><rect x="84" y="63" width="14" height="3.5" rx="1.7"/><rect x="84" y="69" width="14" height="3.5" rx="1.7"/><rect x="66" y="76" width="32" height="3.5" rx="1.7"/><rect x="66" y="82" width="32" height="3.5" rx="1.7"/></g>
  </svg>
  <div class="step-title">Value</div>
  <div class="step-copy">The project must provide<br>value that significantly<br>exceeds potential project<br>costs and should be aligned<br>with the company's strategy.</div>
  <div class="step-btn">Learn More</div>
  <div class="step-num">01</div>
</div>

<div class="step" style="left:189px;top:270px">
  <svg class="tile" viewBox="0 0 162 420"><use href="#tile"/>
    <g fill="#fff"><ellipse cx="81" cy="63" rx="10" ry="12"/><path d="M59 93 Q60 79 72 77 L81 84 L90 77 Q102 79 103 93 Z"/></g>
    <path d="M81 84 L79 93 H83 Z" fill="var(--green)"/>
  </svg>
  <div class="step-title">Capability</div>
  <div class="step-copy">The company and the<br>implementation team<br>must be capable of<br>implementing the project<br>on their own or with help.</div>
  <div class="step-btn">Learn More</div>
  <div class="step-num">02</div>
</div>

<div class="step" style="left:363px;top:270px">
  <svg class="tile" viewBox="0 0 162 420"><use href="#tile"/>
    <g fill="none" stroke="#fff">
      <circle cx="76" cy="78" r="12" stroke-width="6" stroke-dasharray="4 3.5"/>
      <circle cx="94" cy="59" r="7" stroke-width="4" stroke-dasharray="3 2.5"/>
      <circle cx="97" cy="71" r="3.5" stroke-width="2.5" stroke-dasharray="2 1.5"/>
    </g>
    <circle cx="76" cy="78" r="10" fill="#fff"/><circle cx="76" cy="78" r="3.5" fill="none" stroke="var(--green)" stroke-width="2"/>
    <circle cx="94" cy="59" r="5.5" fill="#fff"/><circle cx="94" cy="59" r="2" fill="var(--green)"/>
  </svg>
  <div class="step-title">Functionality</div>
  <div class="step-copy">An ERP project must<br>support required business<br>processes, both now<br>and in the future.</div>
  <div class="step-btn">Learn More</div>
  <div class="step-num">03</div>
</div>

<div class="step" style="left:537px;top:270px">
  <svg class="tile" viewBox="0 0 162 420"><use href="#tile"/>
    <path d="M66 54 H92 L97 59 V94 H66 Z" fill="#fff"/>
    <g fill="var(--green)"><circle cx="74" cy="66" r="3.5"/><rect x="80" y="63" width="2" height="6"/><rect x="84" y="65" width="2" height="4"/><rect x="88" y="61" width="2" height="8"/>
    <rect x="70" y="74" width="22" height="1.6"/><rect x="70" y="78" width="22" height="1.6"/><rect x="70" y="82" width="22" height="1.6"/></g>
  </svg>
  <div class="step-title">Data</div>
  <div class="step-copy">ERP systems are<br>data-hungry creatures.<br>Please be careful before<br>assuming that because so<br>much data goes into them.</div>
  <div class="step-btn">Learn More</div>
  <div class="step-num">04</div>
</div>

<!-- Row two -->
<div class="step" style="left:15px;top:740px">
  <svg class="tile" viewBox="0 0 162 420"><use href="#tile"/>
    <g fill="none" stroke="#fff" stroke-width="2.4" stroke-linecap="round">
      <path d="M65 70 Q66 53 81 52 Q98 53 99 70 Q99 82 94 91"/>
      <path d="M71 74 Q70 59 81 58 Q93 59 93 71 Q93 82 88 90"/>
      <path d="M76 82 Q76 64 81 64 Q87 65 87 72 Q87 83 82 92"/>
      <path d="M81 71 Q81 84 75 92"/><path d="M67 80 Q70 86 68 90"/>
    </g>
  </svg>
  <div class="step-title">Technology</div>
  <div class="step-copy">What is the platform for the<br>system? Is it offered by<br>a vendor that will be<br>around for as long as your<br>system?</div>
  <div class="step-btn">Learn More</div>
  <div class="step-num">05</div>
</div>

<div class="step" style="left:189px;top:740px">
  <svg class="tile" viewBox="0 0 162 420"><use href="#tile"/>
    <g fill="#fff"><path d="M76 50 L78 54 L81 50 L84 54 L86 50 V55 H76 Z"/><circle cx="81" cy="60" r="4.5"/>
    <rect x="75" y="66" width="12" height="8" rx="2"/><rect x="61" y="73" width="40" height="4"/>
    <rect x="61" y="79" width="3.5" height="16"/><rect x="97" y="79" width="3.5" height="16"/>
    <rect x="68" y="79" width="8" height="16"/><rect x="79" y="81" width="4" height="14"/><rect x="86" y="79" width="8" height="16"/></g>
  </svg>
  <div class="step-title">Change Leadership</div>
  <div class="step-copy">Change leadership<br>(often called change<br>management) considers<br>the human side of an<br>ERP implementation.</div>
  <div class="step-btn">Learn More</div>
  <div class="step-num">06</div>
</div>

<div class="step" style="left:363px;top:740px">
  <svg class="tile" viewBox="0 0 162 420"><use href="#tile"/>
    <g fill="#fff"><rect x="66" y="70" width="6" height="22" rx="1"/>
    <path d="M75 70 L82 60 Q83 52 87 53 Q90 55 88 66 H98 Q102 67 101 71 Q100 88 95 92 H75 Z"/></g>
  </svg>
  <div class="step-title">Quality</div>
  <div class="step-copy">Quality is multi-<br>dimensional, and it’s more<br>than a measurement;<br>it’s a perception. An ERP<br>needs to be reliable.</div>
  <div class="step-btn">Learn More</div>
  <div class="step-num">07</div>
</div>

<div class="step" style="left:537px;top:740px">
  <svg class="tile" viewBox="0 0 162 420"><use href="#tile"/>
    <g fill="#fff"><circle cx="68" cy="57" r="3"/><circle cx="75" cy="55" r="3.2"/><circle cx="82" cy="57" r="3"/>
    <rect x="64" y="62" width="8" height="10" rx="2"/><rect x="71" y="61" width="9" height="15" rx="2"/><rect x="79" y="62" width="8" height="10" rx="2"/></g>
    <circle cx="92" cy="82" r="10" fill="none" stroke="#fff" stroke-width="5" stroke-dasharray="3.6 3"/>
    <circle cx="92" cy="82" r="8.5" fill="#fff"/><circle cx="92" cy="82" r="3" fill="var(--green)"/>
  </svg>
  <div class="step-title">Governance</div>
  <div class="step-copy">ERP projects require both<br>management and<br>leadership.</div>
  <div class="step-btn">Learn More</div>
  <div class="step-num">08</div>
</div>

</body>
</html>
```